Tour Guide in Israel business card

I am a tour guide in Israel (the holy land). Prior to it I have over 20 years high-tech business. My main (but not only) focus is working with business people that come to Israel and want to get a tour (usually short from few hours to 2 days). During my guiding I incorporate a lot of my know how of the Israeli business culture. I like to have a business card that I can present to anyone that is looking for a tour guide, but that business people will understand the additional value I can provide them during my tour.

Target Market(s)

Business visitors and tourist to Israel

Industry/Entity Type

Tourism

Contact Information for Business Card

Rory Talbeck
email: rory@talbeck-mail.net
Mobile: +972-52-7164059

Colors

Designer to choose colors to be used in the design.

Requirements
Must have
• Tour Guide
Nice to have
• I don't know how but it should project my understanding in business not just the tourist side of my knowledge.

```html
<!DOCTYPE html>
<html lang="en">
<head>
<meta charset="utf-8">
<title>Tour Guide – Business Card</title>
<link rel="stylesheet" href="https://fonts.googleapis.com/css2?family=Oswald:wght@500&family=Montserrat:wght@400;500&display=swap">
<style>
  :root {
    --stage: #2b2b2b;
    --card-dark: #161616;
    --card-light: #ffffff;
    --brand-blue: #1f74c0;
    --text-grey: #6e6e6e;
    --title-grey: #555555;
    --front-text: #bdbdbd;
  }
  * { margin: 0; padding: 0; box-sizing: border-box; }
  html, body {
    width: 1200px;
    height: 900px;
    overflow: hidden;
    background: var(--stage);
  }
  .canvas {
    width: 1200px;
    height: 900px;
    display: flex;
    flex-direction: column;
    align-items: center;
    justify-content: center;
    gap: 40px;
  }
  .card {
    width: 700px;
    height: 400px;
    position: relative;
    box-shadow: 0 10px 30px rgba(0,0,0,0.45);
  }
  .card--front {
    background: var(--card-dark);
    display: flex;
    align-items: center;
    justify-content: center;
  }
  .front-title {
    font-family: "Montserrat", sans-serif;
    font-weight: 500;
    font-size: 44px;
    letter-spacing: 8px;
    color: var(--front-text);
    white-space: nowrap;
  }
  .card--back {
    background: var(--card-light);
    display: flex;
    align-items: center;
    padding-left: 110px;
  }
  .identity {
    text-align: right;
    width: 190px;
  }
  .identity__name {
    font-family: "Oswald", sans-serif;
    font-weight: 500;
    font-size: 30px;
    line-height: 1;
    color: var(--brand-blue);
    text-transform: uppercase;
    letter-spacing: -0.5px;
    white-space: nowrap;
  }
  .identity__role {
    font-family: "Montserrat", sans-serif;
    font-weight: 500;
    font-size: 13px;
    letter-spacing: 2px;
    color: var(--title-grey);
    margin-top: 4px;
    margin-right: 4px;
  }
  .divider {
    width: 1.5px;
    height: 40px;
    background: var(--brand-blue);
    margin: 0 36px 0 44px;
  }
  .contacts {
    list-style: none;
    font-family: "Montserrat", sans-serif;
    font-size: 19px;
    color: var(--text-grey);
    letter-spacing: 0.5px;
  }
  .contacts__item {
    display: flex;
    align-items: center;
    gap: 14px;
    line-height: 1.35;
  }
  .contacts__icon {
    width: 14px;
    height: 14px;
    flex: none;
  }
</style>
</head>
<body>
<main class="canvas">
  <section class="card card--front" aria-label="Card front">
    <h1 class="front-title">TOUR GUIDE</h1>
  </section>

  <section class="card card--back" aria-label="Card back">
    <div class="identity">
      <p class="identity__name">Rory Talbeck</p>
      <p class="identity__role">DIRECTOR</p>
    </div>
    <div class="divider"></div>
    <ul class="contacts">
      <li class="contacts__item">
        <svg class="contacts__icon" viewBox="0 0 24 24" aria-hidden="true">
          <path fill="#1f74c0" d="M6.6 10.8a15.1 15.1 0 0 0 6.6 6.6l2.2-2.2c.3-.3.7-.4 1-.2 1.1.4 2.3.6 3.6.6.6 0 1 .4 1 1V20c0 .6-.4 1-1 1A17 17 0 0 1 3 4c0-.6.4-1 1-1h3.5c.6 0 1 .4 1 1 0 1.3.2 2.5.6 3.6.1.3 0 .7-.2 1z"/>
        </svg>
        <span>+972-52-7164059</span>
      </li>
      <li class="contacts__item">
        <svg class="contacts__icon" viewBox="0 0 24 24" aria-hidden="true">
          <rect x="2.5" y="5" width="19" height="14" rx="1.5" fill="none" stroke="#1f74c0" stroke-width="2.2"/>
          <path d="M3 6l9 7 9-7" fill="none" stroke="#1f74c0" stroke-width="2.2"/>
        </svg>
        <span>rory@talbeck-mail.net</span>
      </li>
    </ul>
  </section>
</main>
</body>
</html>
```